Willowmere Spa and Beauty Ltd. (Name of business)

I need a business card designed for this new company based out of Toronto Ontario. We specialize in Eyelash Extensions, Manicures and Pedicures, body waxing, massages, laser hair removal and botox treatments. Also offer a variety of products for sale, such as skin cream serums, collagen gel, eye cream, etc. It is a safe relaxing and non-judgemental environnment. Clients are welcome to come be pampered for the half or full day. Many service packages to choose from.

Open 7days per week from 8am to 8pm.

Priscilla Dunmore
Spa Facilitator
Willowmere Spa and Beauty Ltd.
7200 Harcourt St; Suite 1400
Toronto ON K2P 9W4

OFFICE: 416.790.4100
FAX: 416.790.4101
CELL: 416.632.1987
EMAIL: priscilla.dunmore@willowmerespa.com

Target Market(s)

Target market is primarily female ranging from 16 years old to 50 years old.

Industry/Entity Type

Business

Contact Information for Business Card

Priscilla Dunmore
Spa Facilitator
7200 Harcourt St; Suite 1400
Toronto ON K2P 9W4

OFFICE: 416.790.4100
FAX: 416.790.4101
CELL: 416.632.1987

Logo Text

I dont have a logo yet. I would like it simple but sophisticated and modern.

Font styles to use
Serif

Requirements
Must have
• all pertinent details such as company name, logo, name and contact information, services that are offered, including package rates
Nice to have
• Company name and logo prominent. A card that is neat and the information such as address, phone number, fax, email, etc is not too crowded but laid out in an easy to read format.
• Possibly on the back of card - some of the services offered could be listed, as well as professional cream lotions and serums. Hours of operation etc.

```html
<!DOCTYPE html>
<html lang="en">
<head>
<meta charset="utf-8">
<title>Willowmere Spa and Beauty Ltd. — Business Card</title>
<link href="https://fonts.googleapis.com/css2?family=Source+Sans+3:ital,wght@0,300;0,400;0,600;1,400&display=swap" rel="stylesheet">
<style>
  :root {
    --backdrop: #161616;
    --card-white: #ffffff;
    --brand-purple: #a61af0;
    --brand-purple-top: #b118f7;
    --brand-purple-bottom: #780bcf;
    --text-grey: #4a4a4a;
    --on-purple: #ffffff;
  }
  * { margin: 0; padding: 0; box-sizing: border-box; }
  html, body {
    width: 1200px; height: 900px; overflow: hidden;
    background: var(--backdrop);
    font-family: "Source Sans 3", "Myriad Pro", Arial, sans-serif;
  }
  .canvas { position: relative; width: 1200px; height: 900px; }

  .card {
    position: absolute; top: 306px;
    width: 439px; height: 271px;
    border-radius: 12px; overflow: hidden;
  }
  .card--front { left: 149px; background: var(--card-white); }
  .card--back {
    left: 609px;
    background: linear-gradient(180deg, var(--brand-purple-top) 0%, var(--brand-purple-bottom) 100%);
    display: flex; align-items: center; justify-content: center;
  }

  .wordmark-vertical {
    position: absolute; left: 222px; top: 441px;
    transform: translate(-50%, -50%) rotate(-90deg);
    color: var(--brand-purple);
    font-size: 40px; font-weight: 300; letter-spacing: 1px;
    white-space: nowrap; line-height: 1;
  }
  .card--front .wordmark-vertical { left: 73px; top: 135px; }

  .details { position: absolute; left: 164px; top: 42px; color: var(--text-grey); font-size: 12.5px; line-height: 16px; }
  .details__name { color: var(--brand-purple); font-weight: 600; font-size: 15px; line-height: 18px; }
  .details__role { margin-bottom: 10px; }
  .details__address { margin-bottom: 8px; }
  .contact-list { list-style: none; }
  .contact-list li { display: flex; align-items: center; gap: 6px; height: 15px; }
  .contact-list svg { width: 9px; height: 9px; fill: var(--brand-purple); flex: none; }
  .contact-list .contact-email { font-size: 10.5px; }
  .details__hours { margin-top: 19px; color: var(--brand-purple); font-style: italic; font-size: 12.5px; }

  .wordmark-large {
    color: var(--on-purple);
    font-size: 64px; font-weight: 300; letter-spacing: 2px; line-height: 1;
    margin-top: -8px;
  }
</style>
</head>
<body>
<main class="canvas">
  <section class="card card--front" aria-label="Business card front">
    <div class="wordmark-vertical">Willowmere</div>
    <div class="details">
      <p class="details__name">Priscilla Dunmore</p>
      <p class="details__role">Spa Facilitator</p>
      <p class="details__address">Willowmere Spa and Beauty Ltd.<br>7200 Harcourt St; Suite 1400<br>Toronto ON K2P 9W4</p>
      <ul class="contact-list">
        <li><svg viewBox="0 0 10 10" aria-label="Office"><path d="M2 0.5 L3.6 0.5 L4.3 2.8 L3.2 3.8 Q4.2 5.9 6.2 6.8 L7.2 5.7 L9.5 6.4 L9.5 8 Q9.5 9.5 8 9.5 Q0.5 9 0.5 2 Q0.5 0.5 2 0.5 Z"/></svg>416.790.4100</li>
        <li><svg viewBox="0 0 10 10" aria-label="Fax"><path d="M2.5 0.5 H7.5 V3 H2.5 Z M0.5 3.5 H9.5 V9.5 H0.5 Z"/><rect x="2.5" y="5" width="5" height="1.2" fill="#fff"/></svg>416.790.4101</li>
        <li><svg viewBox="0 0 10 10" aria-label="Cell"><path d="M2.5 0.3 H7.5 V9.7 H2.5 Z M3.4 1.3 V7.8 H6.6 V1.3 Z"/></svg>416.632.1987</li>
        <li class="contact-email"><svg viewBox="0 0 10 10" aria-label="Email"><path d="M0.5 2 H9.5 V8.5 H0.5 Z"/><path d="M0.8 2.3 L5 5.6 L9.2 2.3" stroke="#fff" stroke-width="0.9" fill="none"/></svg>priscilla.dunmore@willowmerespa.com</li>
      </ul>
      <p class="details__hours">Open 7days per week from 8am to 8pm.</p>
    </div>
  </section>

  <section class="card card--back" aria-label="Business card back">
    <div class="wordmark-large">Willowmere</div>
  </section>
</main>
</body>
</html>
```